Business Cards and label design needed!

I am a metalsmith, working in sterling silver, brass and moving slowly into adding some gold accent pieces. I also use patinas to add color to brass pieces. The peacock feather is used in my packaging, as both a label and tissue paper. I am attaching what I am currently using, and printing at home, but I need a design that I can have professionally printed. My website is www.fernhollowworks.com
Target Market(s)
Established Professionals, Independent thinkers, Art donors, Artist supporters
Industry/Entity Type
Jewelry
Contact Information for Business Card
I would like a business card with the basic contact information, including Folio and Lens. I currently use a peacock feather and would like to continue that. I like to use turquoise, Tiffany blue and colors in that direction. I am open to other suggestions. I would like to be able to transfer the design to oval labels as well.
Other font styles liked:
- Garamond or other fonts that have a slight script that is easy to read
Look and feel

```html
<!DOCTYPE html>
<html lang="en">
<head>
<meta charset="utf-8">
<title>Fern Hollow Works – Business Card</title>
<link rel="stylesheet" href="https://fonts.googleapis.com/css2?family=Roboto:wght@400;500;700&display=swap">
<style>
  :root {
    --backdrop: #e6e6e8;
    --card-front: #c9ece6;
    --card-back: #fbfbfa;
    --navy: #233a7a;
    --navy-text: #1f3a7d;
    --mint: #b5e3d3;
    --mint-soft: #d3efe5;
    --teal-mark: #5cbfbc;
    --white: #ffffff;
  }
  * { margin: 0; padding: 0; box-sizing: border-box; }
  html, body {
    width: 1200px; height: 1200px; overflow: hidden;
    background: var(--backdrop);
    font-family: "Roboto", Arial, sans-serif;
    color: var(--navy-text);
  }
  .canvas { position: relative; width: 1200px; height: 1200px; }
  .card {
    position: absolute; border-radius: 22px; overflow: hidden;
  }
  .card-front {
    left: 238px; top: 118px; width: 712px; height: 419px;
    background: var(--card-front);
  }
  .card-back {
    left: 231px; top: 645px; width: 726px; height: 415px;
    background: var(--card-back);
  }
  .brand-mark {
    position: absolute; border-radius: 50%; background: var(--teal-mark);
  }
  .brand-name {
    position: absolute; font-weight: 400; color: var(--navy-text);
    white-space: nowrap; transform: translateX(-50%);
  }
  .card-front .brand-mark { left: 334px; top: 130px; width: 44px; height: 44px; }
  .card-front .brand-name { left: 356px; top: 236px; font-size: 44px; }
  .card-front .website {
    position: absolute; left: 0; right: 0; top: 380px;
    text-align: center; font-size: 16px;
  }
  .card-back .brand-mark { left: 540px; top: 62px; width: 40px; height: 40px; }
  .card-back .brand-name { left: 522px; top: 150px; font-size: 34px; }
  .holder { position: absolute; left: 43px; top: 70px; }
  .holder-name { font-size: 25px; font-weight: 500; }
  .holder-title { font-size: 15px; margin-top: 6px; }
  .contact-list {
    position: absolute; left: 40px; top: 238px; list-style: none;
    font-size: 17px; line-height: 24.5px;
  }
  .contact-list li { display: flex; align-items: center; gap: 20px; }
  .contact-list svg { width: 17px; height: 17px; fill: var(--navy-text); }
  .wave { position: absolute; left: 0; top: 0; }
  .social {
    position: absolute; left: 482px; top: 356px;
    display: flex; align-items: center; gap: 12px;
    color: var(--white); font-size: 16px;
  }
  .social-item { display: flex; align-items: center; gap: 6px; }
  .social-dot { width: 14px; height: 14px; border-radius: 50%; background: var(--white); }
</style>
</head>
<body>
<main class="canvas">
  <section class="card card-front">
    <div class="brand-mark" aria-hidden="true"></div>
    <div class="brand-name">Fern Hollow Works</div>
    <div class="website">www.fernhollowworks.com</div>
  </section>

  <section class="card card-back">
    <svg class="wave" width="726" height="415" viewBox="0 0 726 415" aria-hidden="true">
      <path d="M0 330 C150 385 330 395 470 330 C560 290 650 278 726 285 L726 298 C650 292 560 305 470 345 C330 405 150 395 0 345 Z" fill="var(--mint)"/>
      <path d="M40 345 C180 385 330 385 460 348 L460 356 C330 392 180 392 40 345 Z" fill="var(--mint-soft)"/>
      <path d="M0 370 C150 398 320 400 470 345 C570 308 660 300 726 305 L726 415 L0 415 Z" fill="var(--navy)"/>
    </svg>

    <div class="brand-mark" aria-hidden="true"></div>
    <div class="brand-name">Fern Hollow Works</div>

    <div class="holder">
      <div class="holder-name">Maren Holt</div>
      <div class="holder-title">Managing Director</div>
    </div>

    <ul class="contact-list">
      <li>
        <svg viewBox="0 0 24 24" aria-hidden="true"><path d="M3 9c0-3 4-5 9-5s9 2 9 5v2h-5V9H8v2H3zM7 12h10l3 8H4z"/></svg>
        <span>555.014.2093</span>
      </li>
      <li>
        <svg viewBox="0 0 24 24" aria-hidden="true"><path d="M2 5h20v14H2zM4 7v1l8 5 8-5V7l-8 5z"/></svg>
        <span>studio@fernhollowworks.com</span>
      </li>
      <li>
        <svg viewBox="0 0 24 24" aria-hidden="true"><path d="M12 2a10 10 0 1 0 0 20 10 10 0 0 0 0-20zm-1 2.1V8H7.6A8 8 0 0 1 11 4.1zm2 0A8 8 0 0 1 16.4 8H13zM4.3 10H11v4H4.3a8 8 0 0 1 0-4zM13 10h6.7a8 8 0 0 1 0 4H13zM7.6 16H11v3.9A8 8 0 0 1 7.6 16zm5.4 0h3.4a8 8 0 0 1-3.4 3.9z"/></svg>
        <span>www.fernhollowworks.com</span>
      </li>
    </ul>

    <div class="social">
      <span>Follow us on:</span>
      <span class="social-item"><span class="social-dot"></span>Folio</span>
      <span class="social-item">Lens</span>
    </div>
  </section>
</main>
</body>
</html>
```